Talvern Asset Management - Corporate Letter Head Project

Looking for a classy design based on our current logo. Please find current logo source file in files. With our color scheme.

Target Market(s)

We're an investment firm, the letterhead needs to look professional and attractive to clients.

Industry/Entity Type

Hedgefund

Colors
0054AA
0677BA
7BADD7
CADEEF
E8F1F8

Requirements
Must have
• Our logo, address, phone number, and email

```html
<!DOCTYPE html>
<html lang="en">
<head>
<meta charset="utf-8">
<title>Talvern Asset Management – Letterhead</title>
<link href="https://fonts.googleapis.com/css2?family=Arimo:wght@400&family=Cormorant+Garamond:wght@500&display=swap" rel="stylesheet">
<style>
  :root {
    --paper: #f5f3f4;
    --ink: #3a3a3a;
    --ink-soft: #4a4a4a;
    --brand-navy: #1c2a44;
    --brand-blue: #0054aa;
    --contact: #1a1a1a;
  }
  * { margin: 0; padding: 0; box-sizing: border-box; }
  html, body { width: 935px; height: 1200px; overflow: hidden; background: var(--paper); }
  .letterhead {
    position: relative;
    width: 935px; height: 1200px;
    background: var(--paper);
    font-family: "Arimo", Arial, sans-serif;
    color: var(--ink);
  }
  .brand {
    position: absolute; left: 89px; top: 70px;
    display: flex; flex-direction: column; align-items: center; gap: 12px;
  }
  .brand-mark {
    width: 58px; height: 58px;
    border: 2px solid var(--brand-navy);
  }
  .brand-name {
    font-family: "Cormorant Garamond", Georgia, serif;
    font-weight: 500; font-size: 24px; line-height: 24px;
    color: var(--brand-navy); text-align: center; letter-spacing: 1px;
    text-transform: uppercase;
  }
  .contact {
    position: absolute; left: 676px; top: 99px;
    font-size: 14px; line-height: 17.5px; color: var(--contact);
  }
  .contact-gap { height: 8px; }
  .contact-line { display: flex; align-items: center; gap: 5px; }
  .contact-line svg { width: 11px; height: 11px; fill: var(--brand-navy); flex: none; }
  .salutation {
    position: absolute; left: 93px; top: 307px;
    font-size: 24px; color: var(--ink-soft);
  }
  .letter-body {
    position: absolute; left: 93px; top: 380px; width: 753px;
    font-size: 13.6px; line-height: 20.5px; text-align: justify;
  }
  .letter-body p + p { margin-top: 18px; }
  .closing {
    position: absolute; left: 93px; top: 830px;
    font-size: 13.6px;
  }
  .signature {
    position: absolute; left: 90px; top: 858px;
    width: 120px; height: 50px;
    background: linear-gradient(90deg, rgba(30,30,40,0.15), rgba(30,30,40,0.05));
  }
  .signatory {
    position: absolute; left: 98px; top: 926px;
  }
  .signatory-name { font-size: 18px; color: var(--ink-soft); }
  .signatory-title { font-size: 14px; margin-top: 6px; color: var(--ink-soft); }
</style>
</head>
<body>
<main class="letterhead">
  <header>
    <div class="brand">
      <div class="brand-mark"></div>
      <div class="brand-name">Talvern Asset<br>Management</div>
    </div>
    <address class="contact" style="font-style:normal">
      <div>4820 Larkfield Ct</div>
      <div>210B Millbrook</div>
      <div>IN 46591</div>
      <div class="contact-gap"></div>
      <div class="contact-line">
        <svg viewBox="0 0 24 24" aria-hidden="true"><path d="M6.6 10.8a15.1 15.1 0 0 0 6.6 6.6l2.2-2.2a1 1 0 0 1 1-.25 11.4 11.4 0 0 0 3.6.57 1 1 0 0 1 1 1V20a1 1 0 0 1-1 1A17 17 0 0 1 3 4a1 1 0 0 1 1-1h3.5a1 1 0 0 1 1 1c0 1.25.2 2.45.57 3.6a1 1 0 0 1-.25 1z"/></svg>
        <span>5745550182</span>
      </div>
      <div class="contact-line">
        <svg viewBox="0 0 24 24" aria-hidden="true"><path d="M2 5h20v14H2z M3 6l9 7 9-7" fill="var(--brand-navy)"/><path d="M3 6.5l9 6.5 9-6.5" stroke="#fff" stroke-width="1.6" fill="none"/></svg>
        <span>info@TalvernAsset.com</span>
      </div>
    </address>
  </header>

  <h1 class="salutation" style="font-weight:400">Dear Mr. Hale,</h1>

  <section class="letter-body">
    <p>Lorem ipsum dolor sit amet, consectetur adipiscing elit. Donec orci purus, luctus vitae dignissim eu, iaculis sed purus. Vivamus faucibus, ipsum nec aliquet viverra, leo mauris condimentum ligula, sit amet sagittis enim ligula quis arcu. Nam egestas tortor id nisi porttitor mattis. In tortor ante, ultricies in suscipit a, tempus non massa. Vivamus et auctor mi. Fusce vel massa nulla. Phasellus nec eros mauris, et scelerisque orci.</p>
    <p>Donec malesuada orci vitae nulla accumsan porta a id massa. Quisque accumsan iaculis magna sit amet fringilla. Maecenas consequat, magna eget tincidunt semper, odio nibh rutrum mi, id feugiat ante nisi eu risus. Vestibulum nunc orci, rhoncus a placerat in, ultricies in mi. Cras mattis varius eros, vel fringilla nisi suscipit eget. Quisque scelerisque sagittis nulla at porttitor.</p>
    <p>Sed id augue vitae urna euismod commodo aliquet a quam. Pellentesque arcu velit, cursus et malesuada ut, consequat et diam. Nullam erat sem, rhoncus id ullamcorper vitae, rhoncus et arcu. In ultricies ultricies nulla, ut rutrum nisi iaculis at. Donec eu magna a metus ornare faucibus. Fusce aliquet faucibus ultricies. Morbi semper, est id tincidunt gravida, sem arcu adipiscing lacus, ac bibendum nulla leo eu purus. Quisque nec diam sed risus consectetur a ccumsan quis quis nibh. Vestibulum id purus lorem.</p>
    <p>It is a long established fact that a reader will be distracted by the readable content of a page when looking at its layout. The point of using Lorem Ipsum is that it has a more-or-less normal distribution of letters, as opposed to using 'Content here, content here', making it look like readable English. Many desktop publishing packages</p>
  </section>

  <footer>
    <div class="closing">Sincerely,</div>
    <div class="signature" role="img" aria-label="Handwritten signature of Daniel Hale"></div>
    <div class="signatory">
      <div class="signatory-name">Daniel Hale</div>
      <div class="signatory-title">CEO/ Founder</div>
    </div>
  </footer>
</main>
</body>
</html>
```